Delivery Docket urgent plus require many other designs for more stationary after this.

We need a new delivery docket design urgently as the one we have needs updating and we have changed our company name. Please do not copy the one I have uploaded as we do not feel this looks professional enough. I uploaded it as a few designers requested to see what we are currently using thank you.
It is quite complex in that we need a range of information to be on the one docket.
We are a Transport Company based in Australia that has a wide variety of items that we deliver such as water, sand and gravels and heavy equipment transport.
We would prefer to keep this design to A5 size as we will get them made into books. We are looking for a modern professional look. Although it is only a delivery docket this is given to all our customers so needs to look impressive.

We need our new logo on the docket (PRW). There will also need to be areas for our address and contact numbers, email etc these will be supplied to the winning designer to make the final adjustments so for now just put something generic in these spaces.
Needs to have an area for customer details, purchase order number, date and docket number (docket number to be in red)
Needs a section where we can list the type of product / and or service that has been provided and the amount / qty usually 3 lines will be enough for this. Need area under this where the customer can sign name and print name to say that the goods / and or services have been received.

Also required somewhere on the docket are the words, Tax Invoice will be issued based on the information provided on this docket. Conditions on back of page

We then need a separate section on the same page which we will use internally that the staff member can tear off and hand into the office. On this section it needs to have area where the driver can list km at start of job and at end with space to calculate km travelled, details of fuel purchased eg amount and litres, vehicle that is being used. also need to log down wheel bearing temps.
prime mover needs spaces as follows
Steer axel FL____________ Steer axel FR _________ 1st drive axel L_______
1st drive axel R_________ 2nd drive axel L_______ 2nd drive axel R________

For the trailers need something similar x 2 as have 2 trailers
1st axel DS_________ 1st axel PS_________ 2nd axel DS__________
2nd axel PS_________ 3rd axel DS_________ 3rd axel PS__________

I have included a few examples of designs we have used in past and ones that we like so you can get an idea of the colours we prefer, I have included some of the designs we are currently receiving for our logo that I like so you can get idea again of colours we prefer. There is much more we need designed also such as time sheets, more delivery dockets and letter heads so there is a lot of more work available to the winning designer.

Thank you

Target Market(s)

Customers

Font styles to use
Serif
Sans Serif

Colors

Designer to choose colors to be used in the design.

Requirements
Should not have
• Please don't copy old docket as we do not like it and nned new info on new design thank you

```html
<!DOCTYPE html>
<html lang="en">
<head>
<meta charset="utf-8">
<title>PRW Delivery Docket</title>
<link rel="stylesheet" href="https://fonts.googleapis.com/css2?family=Mulish:wght@400;600;700;800;900&display=swap">
<style>
  :root {
    --bg: #d2d2d2;
    --paper: #ffffff;
    --ink: #1f1f1f;
    --dark: #262626;
    --red: #c40d12;
    --red-line: #cf2a2e;
    --rule: #8a8a8a;
    --white: #ffffff;
  }
  * { box-sizing: border-box; margin: 0; padding: 0; }
  html, body { width: 1200px; height: 582px; overflow: hidden; background: var(--bg); }
  body { font-family: "Mulish", Arial, sans-serif; color: var(--ink); position: relative; }

  .docket {
    position: absolute; left: 412px; top: 25px;
    width: 468px; height: 665px;
    transform: scale(0.8); transform-origin: 0 0;
    background: var(--paper);
    box-shadow: 0 4px 10px rgba(0,0,0,0.18);
    overflow: hidden;
  }
  .band { position: absolute; left: 0; width: 468px; }
  .band--top { top: 0; height: 80px; }
  .band--bottom { bottom: 0; height: 48px; }

  .contact-block { position: absolute; left: 16px; top: 15px; color: var(--white); font-size: 7.5px; line-height: 15px; font-weight: 600; }

  .brand { position: absolute; left: 360px; top: 14px; display: flex; align-items: center; gap: 6px; }
  .brand__name { font-size: 34px; font-weight: 900; color: var(--ink); letter-spacing: 1px; line-height: 1; }

  .panel { position: absolute; left: 16px; width: 436px; border: 1px solid var(--red-line); border-radius: 6px; overflow: hidden; }
  .row { display: flex; border-top: 1px solid var(--red-line); height: 21px; }
  .row:first-child { border-top: none; }
  .cell { font-size: 7.5px; font-weight: 600; display: flex; align-items: center; padding-left: 10px; }
  .cell + .cell { border-left: 1px solid var(--red-line); }

  .customer { top: 101px; }
  .customer .half { width: 217px; }
  .customer .half + .half { width: 219px; }
  .head-red { background: var(--red); color: var(--white); font-size: 11px; font-weight: 800; }
  .head-plain { font-size: 11px; font-weight: 800; }
  .docket-no { color: var(--red); margin-left: 5px; }
  .customer .row { height: 21.5px; }

  .products { top: 205px; }
  .products .head-row { background: var(--red); color: var(--white); border: none; }
  .products .head-row .cell { font-size: 11px; font-weight: 800; border-left: none; }
  .col-type { width: 148px; }
  .col-desc { width: 232px; }
  .col-qty { width: 56px; }
  .products .head-row .col-desc { justify-content: center; padding-left: 0; }
  .products .head-row .col-qty { justify-content: center; padding-left: 0; }
  .note { border-top: 1px solid var(--red-line); text-align: center; font-size: 7.5px; font-weight: 600; line-height: 14px; padding: 4px 0 3px; }

  .driver-log { position: absolute; left: 16px; top: 340px; width: 436px; list-style: none; }
  .driver-log li { display: flex; align-items: flex-end; font-size: 7.5px; font-weight: 600; height: 20px; }
  .driver-log .num { color: var(--red); font-weight: 800; width: 13px; }
  .blank { display: inline-block; border-bottom: 1px solid var(--rule); height: 9px; margin: 0 3px; }
  .fill { flex: 1; border-bottom: 1px solid var(--rule); height: 9px; margin-left: 6px; }

  .axles .row { height: 21.5px; }
  .axles .cell { width: 145px; }
  .axles .cell:last-child { width: 146px; }
  .axles--prime { top: 445px; }
  .axles--trailer-one { top: 505px; }
  .axles--trailer-two { top: 565px; }
</style>
</head>
<body>
  <main class="docket">
    <svg class="band band--top" viewBox="0 0 468 80" aria-hidden="true">
      <polygon points="0,0 366,0 272,60 0,60" fill="var(--dark)"/>
      <polygon points="0,66 256,66 372,0 378,0 259,70 0,70" fill="var(--red)"/>
    </svg>

    <div class="contact-block">
      <p>Address :</p>
      <p>Contact Numbers :</p>
      <p>E-mail :</p>
    </div>

    <div class="brand"><span class="brand__name">PRW</span></div>

    <section class="panel customer">
      <div class="row">
        <div class="cell half head-red">CUSTOMER DETAILS</div>
        <div class="cell half head-plain">DELIVERY DOCKET&nbsp;&nbsp;:<span class="docket-no">2050</span></div>
      </div>
      <div class="row"><div class="cell half">Name&nbsp;&nbsp;:</div><div class="cell half">Date&nbsp;&nbsp;:</div></div>
      <div class="row"><div class="cell half">Purchase order number&nbsp;&nbsp;:</div><div class="cell half">Contact&nbsp;&nbsp;:</div></div>
      <div class="row"><div class="cell">Billing Address&nbsp;&nbsp;:</div></div>
    </section>

    <section class="panel products">
      <div class="row head-row">
        <div class="cell col-type">TYPE OF PRODUCT</div>
        <div class="cell col-desc">DESCRIPTION</div>
        <div class="cell col-qty">QTY</div>
      </div>
      <div class="row"><div class="cell col-type"></div><div class="cell col-desc"></div><div class="cell col-qty"></div></div>
      <div class="row"><div class="cell col-type"></div><div class="cell col-desc"></div><div class="cell col-qty"></div></div>
      <div class="row"><div class="cell col-type"></div><div class="cell col-desc"></div><div class="cell col-qty"></div></div>
      <p class="note">Tax Invoice will be issued based on the information provided on this docket.<br>Conditions on back of page.</p>
    </section>

    <ol class="driver-log">
      <li><span class="num">1.</span><span class="blank" style="width:34px;margin-left:0"></span>km at start of job and<span class="blank" style="width:34px"></span>at end<span class="blank" style="width:40px"></span>km travelled.</li>
      <li><span class="num">2.</span>Details of fuel purchased eg amount and litres&nbsp;&nbsp;:<span class="fill"></span></li>
      <li><span class="num">3.</span>Vehicle that is being used&nbsp;&nbsp;:<span class="fill"></span></li>
      <li><span class="num">4.</span>Wheel bearing temps&nbsp;&nbsp;:<span class="fill"></span></li>
    </ol>

    <section class="panel axles axles--prime">
      <div class="row"><div class="cell">Steer axel FL&nbsp;&nbsp;:</div><div class="cell">Steer axel FR&nbsp;&nbsp;:</div><div class="cell">1st drive axel L&nbsp;&nbsp;:</div></div>
      <div class="row"><div class="cell">1st drive axel R&nbsp;&nbsp;:</div><div class="cell">2nd drive axel L&nbsp;&nbsp;:</div><div class="cell">2nd drive axel R&nbsp;&nbsp;:</div></div>
    </section>

    <section class="panel axles axles--trailer-one">
      <div class="row"><div class="cell">1st axel DS&nbsp;&nbsp;:</div><div class="cell">1st axel PS&nbsp;&nbsp;:</div><div class="cell">2nd axel DS&nbsp;&nbsp;:</div></div>
      <div class="row"><div class="cell">2nd axel PS&nbsp;&nbsp;:</div><div class="cell">3rd axel DS&nbsp;&nbsp;:</div><div class="cell">3rd axel PS&nbsp;&nbsp;:</div></div>
    </section>

    <section class="panel axles axles--trailer-two">
      <div class="row"><div class="cell">1st axel DS&nbsp;&nbsp;:</div><div class="cell">1st axel PS&nbsp;&nbsp;:</div><div class="cell">2nd axel DS&nbsp;&nbsp;:</div></div>
      <div class="row"><div class="cell">2nd axel PS&nbsp;&nbsp;:</div><div class="cell">3rd axel DS&nbsp;&nbsp;:</div><div class="cell">3rd axel PS&nbsp;&nbsp;:</div></div>
    </section>

    <svg class="band band--bottom" viewBox="0 0 468 48" aria-hidden="true">
      <polygon points="0,22 234,4 468,22 468,25 234,8 0,25" fill="var(--red)"/>
      <polygon points="0,30 234,13 468,30 468,48 0,48" fill="var(--dark)"/>
    </svg>
  </main>
</body>
</html>
```